Card Design Project Falcrest Spares

We are needing a new backing card for one of our products, this card goes in a plastic clamshel tub and is basically the information card/label for our product. The product is motorcycle fork oil seals and dust sealsm we have our logo that needs to be on it, the words Fork Oil Seals & Dust Seals Kit, we have certain colours that we use.

The design must be print ready, our finished card size is 128mm wide x 94mm with rounded corners, printed on card, gloss finish.
Updates

Target Market(s)

Our target market is motorcyclists of all ages

Industry/Entity Type

Plastic

Requirements
Must have
• Must have our Falcrest Spares logo on it (see uploaded logo)
The main colour of the card must be Orange we use a specific orange colour for these which is Pantone 7-1-7 C or (R =255 G= 134 B=0).
Must have the words 'Fork Oil Seals & Dust Seals'.
And a mention that it 'Includes Fitment Grease'
Also a mention of our four world websites:-

www.falcrestspares.co.uk (UK)
www.falcrest-spares.com (USA)
www.falcrestspares.co.nz (NZ)
www.falcrestspares.com.au (AUS)

```html
<!DOCTYPE html>
<html lang="en">
<head>
<meta charset="utf-8">
<title>Falcrest Spares – Fork Oil Seals &amp; Dust Seals</title>
<link rel="stylesheet" href="https://fonts.googleapis.com/css2?family=Libre+Franklin:wght@800;900&display=swap">
<style>
  :root {
    --card-orange: #f58a22;
    --hero-red: #e0240f;
    --hero-deep: #b8180c;
    --logo-navy: #1c3f8f;
    --panel-white: #ffffff;
    --ink: #111111;
    --text-white: #ffffff;
  }
  * { margin: 0; padding: 0; box-sizing: border-box; }
  html, body {
    width: 1200px;
    height: 881px;
    overflow: hidden;
    background: var(--panel-white);
  }
  .card {
    position: absolute;
    left: 8px;
    top: 8px;
    width: 1184px;
    height: 865px;
    border-radius: 30px;
    background: var(--card-orange);
    overflow: hidden;
    font-family: "Libre Franklin", Arial, sans-serif;
  }
  .motorcycle-art {
    position: absolute;
    inset: 0;
    background:
      radial-gradient(ellipse 42% 55% at 22% 45%, rgba(184,24,12,0.75), rgba(224,36,15,0.45) 55%, rgba(245,138,34,0) 100%),
      radial-gradient(ellipse 38% 60% at 82% 42%, rgba(184,24,12,0.7), rgba(224,36,15,0.4) 55%, rgba(245,138,34,0) 100%),
      linear-gradient(180deg, rgba(245,138,34,0) 0%, rgba(224,36,15,0.55) 30%, rgba(224,36,15,0.5) 60%, rgba(245,138,34,0) 85%);
  }
  .brand-panel {
    position: absolute;
    left: 414px;
    top: 52px;
    width: 356px;
    height: 268px;
    background: var(--panel-white);
    border-radius: 22px;
    box-shadow: 0 0 0 6px rgba(245,138,34,0.6);
    display: flex;
    flex-direction: column;
    align-items: center;
    justify-content: center;
    gap: 28px;
  }
  .brand-dot {
    width: 120px;
    height: 120px;
    border-radius: 50%;
    background: var(--hero-red);
  }
  .brand-name {
    font-weight: 900;
    font-size: 31px;
    color: var(--logo-navy);
    text-transform: uppercase;
    white-space: nowrap;
    text-align: center;
  }
  .outlined {
    position: absolute;
    left: 0;
    width: 100%;
    text-align: center;
    color: var(--text-white);
    font-weight: 900;
    -webkit-text-stroke: 10px var(--ink);
    paint-order: stroke fill;
    white-space: nowrap;
  }
  .headline {
    font-size: 124px;
    line-height: 1;
    letter-spacing: -1px;
  }
  .headline-top { top: 352px; }
  .headline-bottom { top: 506px; }
  .subline {
    top: 656px;
    font-size: 66px;
    line-height: 1;
    letter-spacing: -0.5px;
    -webkit-text-stroke: 8px var(--ink);
  }
  .web-list {
    position: absolute;
    left: 0;
    top: 752px;
    width: 100%;
    display: grid;
    grid-template-columns: auto auto;
    justify-content: center;
    column-gap: 48px;
    row-gap: 10px;
    list-style: none;
  }
  .web-address {
    color: var(--text-white);
    font-weight: 800;
    font-size: 27px;
    line-height: 1.1;
    -webkit-text-stroke: 5px var(--ink);
    paint-order: stroke fill;
    white-space: nowrap;
    text-align: center;
  }
</style>
</head>
<body>
  <main class="card">
    <div class="motorcycle-art" role="img" aria-label="Red silhouette of a classic motorcycle spanning the card"></div>
    <div class="brand-panel">
      <div class="brand-dot"></div>
      <div class="brand-name">Falcrest Spares</div>
    </div>
    <h1 class="outlined headline headline-top">Fork Oil Seals</h1>
    <p class="outlined headline headline-bottom">&amp; Dust Seals</p>
    <p class="outlined subline">Includes Fitment Grease</p>
    <ul class="web-list">
      <li class="web-address">www.falcrestspares.co.uk (UK)</li>
      <li class="web-address">www.falcrest-spares.com (USA)</li>
      <li class="web-address">www.falcrestspares.co.nz (NZ)</li>
      <li class="web-address">www.falcrestspares.com.au (AUS)</li>
    </ul>
  </main>
</body>
</html>
```